Supplement Company Needs a Protein Powder Pouch Design

We are looking for a modern and fresh design for our 500g pouches of protein powder as our current design is not eye catching or exciting enough.

This new design will be printed on both sides of a 178mm x 280mm x 101mm pouch.

We have 4 flavours. These are Banana Ice Cream, Chocolate Deluxe, Strawberries & Cream and Vanilla Ice Cream.

Industry/Entity Type

Supplement

Requirements
Must have
• Attractive and eye catching front and space for all the nutritional information and ingredients on the back.

Must clearly state 'food supplement' somewhere on the front of the pouch.
Nice to have
• Our logo is attached.
Should not have
• No health claims as these are not allowed in the UK

```html
<!DOCTYPE html>
<html lang="en">
<head>
<meta charset="utf-8">
<title>Protein Powder Pouch Range</title>
<link rel="stylesheet" href="https://fonts.googleapis.com/css2?family=Montserrat:wght@700;800&family=Oswald:wght@500&display=swap">
<style>
  :root {
    --page: #ffffff;
    --pouch-black: #141414;
    --pouch-sheen: #262626;
    --stripe-blue: #5bb1da;
    --text-white: #ffffff;
    --chocolate: #a8683f;
    --vanilla: #dba86f;
    --strawberry: #e4373b;
    --banana: #d5ea3b;
  }
  * { box-sizing: border-box; margin: 0; padding: 0; }
  html, body { width: 1200px; height: 600px; overflow: hidden; background: var(--page); }
  .range { position: relative; width: 1200px; height: 600px; }

  .pouch {
    position: absolute; top: 100px; width: 270px; height: 425px;
    background: linear-gradient(200deg, var(--pouch-sheen) 0%, var(--pouch-black) 45%, var(--pouch-black) 100%);
    overflow: hidden; border-radius: 3px;
  }
  .pouch--chocolate { left: 34px; --flavour: var(--chocolate); }
  .pouch--vanilla { left: 324px; --flavour: var(--vanilla); }
  .pouch--strawberry { left: 614px; --flavour: var(--strawberry); }
  .pouch--banana { left: 904px; --flavour: var(--banana); }

  .side-band { position: absolute; left: 0; top: 0; width: 58px; height: 100%; background: var(--flavour); }
  .side-stripe {
    position: absolute; left: 58px; top: 0; width: 10px; height: 100%;
    background: linear-gradient(180deg, var(--stripe-blue) 0%, var(--stripe-blue) 45%, var(--flavour) 75%, var(--flavour) 100%);
  }
  .side-label {
    position: absolute; left: 29px; top: 325px; transform-origin: 0 0; transform: rotate(-90deg) translateY(-50%);
    font-family: "Montserrat", sans-serif; font-weight: 700; font-size: 21px; letter-spacing: 0.5px;
    color: var(--text-white); white-space: nowrap;
  }

  .brand {
    position: absolute; right: 33px; top: 150px; display: flex; align-items: center; gap: 4px;
    font-family: "Montserrat", sans-serif; font-weight: 800; font-size: 14px; color: var(--text-white);
  }
  .brand-dot { width: 7px; height: 7px; border-radius: 50%; background: var(--text-white); }

  .product-name {
    position: absolute; left: 84px; width: 155px; top: 178px; text-align: center;
    font-family: "Montserrat", sans-serif; font-weight: 800; line-height: 1;
  }
  .product-name__main { display: block; font-size: 34px; color: var(--text-white); letter-spacing: -0.5px; }
  .product-name__sub { display: block; margin-top: 4px; font-size: 25px; color: var(--flavour); }

  .flavour-tag {
    position: absolute; left: 90px; top: 279px; width: 110px; height: 34px; padding: 5px 0 0 9px;
    background: linear-gradient(90deg, transparent 0%, var(--flavour) 60%);
    font-family: "Oswald", sans-serif; font-weight: 500; font-size: 10.5px; line-height: 1.1;
    color: var(--text-white); text-transform: uppercase; white-space: nowrap; z-index: 2;
  }
  .flavour-image {
    position: absolute; left: 188px; top: 276px; width: 60px; height: 60px; border-radius: 50%;
    background: radial-gradient(circle at 40% 35%, #fff8e8 0%, var(--flavour) 90%); z-index: 1;
  }
  .pouch--chocolate .flavour-image { border-radius: 10px; background: linear-gradient(135deg, #8b5433, #4a2a17); }

  .nutrition { position: absolute; left: 164px; top: 358px; display: flex; gap: 3px; }
  .nutrition-badge {
    width: 17px; height: 17px; border: 1px solid var(--text-white); border-radius: 3px;
    font-family: "Oswald", sans-serif; color: var(--text-white); text-align: center; line-height: 1;
  }
  .nutrition-badge b { display: block; font-size: 5px; font-weight: 500; margin-top: 2px; }
  .nutrition-badge span { display: block; font-size: 2.6px; margin-top: 1px; }
  .net-weight {
    position: absolute; left: 164px; width: 57px; top: 380px; text-align: center;
    font-family: "Oswald", sans-serif; font-weight: 500; font-size: 6px; color: var(--text-white);
  }
</style>
</head>
<body>
<main class="range">

  <article class="pouch pouch--chocolate">
    <div class="side-band"></div><div class="side-stripe"></div>
    <p class="side-label">FOOD SUPPLEMENT</p>
    <div class="brand"><span class="brand-dot"></span>Brisk Supplements</div>
    <h2 class="product-name"><span class="product-name__main">PROTEIN</span><span class="product-name__sub">POWDER</span></h2>
    <p class="flavour-tag">Chocolate Deluxe<br>Flavours</p>
    <div class="flavour-image" role="img" aria-label="Photo of broken milk chocolate pieces"></div>
    <div class="nutrition">
      <div class="nutrition-badge"><b>XXX</b><span>CALORIES PER SERVING</span></div>
      <div class="nutrition-badge"><b>XXX</b><span>CARBS PER SERVING</span></div>
      <div class="nutrition-badge"><b>XXX</b><span>PROTEIN PER SERVING</span></div>
    </div>
    <p class="net-weight">NT WT: 500g</p>
  </article>

  <article class="pouch pouch--vanilla">
    <div class="side-band"></div><div class="side-stripe"></div>
    <p class="side-label">FOOD SUPPLEMENT</p>
    <div class="brand"><span class="brand-dot"></span>Brisk Supplements</div>
    <h2 class="product-name"><span class="product-name__main">PROTEIN</span><span class="product-name__sub">POWDER</span></h2>
    <p class="flavour-tag">Vanilla Ice Cream<br>Flavours</p>
    <div class="flavour-image" role="img" aria-label="Photo of a vanilla ice cream scoop with vanilla flowers"></div>
    <div class="nutrition">
      <div class="nutrition-badge"><b>XXX</b><span>CALORIES PER SERVING</span></div>
      <div class="nutrition-badge"><b>XXX</b><span>CARBS PER SERVING</span></div>
      <div class="nutrition-badge"><b>XXX</b><span>PROTEIN PER SERVING</span></div>
    </div>
    <p class="net-weight">NT WT: 500g</p>
  </article>

  <article class="pouch pouch--strawberry">
    <div class="side-band"></div><div class="side-stripe"></div>
    <p class="side-label">FOOD SUPPLEMENT</p>
    <div class="brand"><span class="brand-dot"></span>Brisk Supplements</div>
    <h2 class="product-name"><span class="product-name__main">PROTEIN</span><span class="product-name__sub">POWDER</span></h2>
    <p class="flavour-tag">Strawberries &amp;<br>Cream Flavours</p>
    <div class="flavour-image" role="img" aria-label="Photo of a strawberry ice cream scoop with fresh strawberries"></div>
    <div class="nutrition">
      <div class="nutrition-badge"><b>XXX</b><span>CALORIES PER SERVING</span></div>
      <div class="nutrition-badge"><b>XXX</b><span>CARBS PER SERVING</span></div>
      <div class="nutrition-badge"><b>XXX</b><span>PROTEIN PER SERVING</span></div>
    </div>
    <p class="net-weight">NT WT: 500g</p>
  </article>

  <article class="pouch pouch--banana">
    <div class="side-band"></div><div class="side-stripe"></div>
    <p class="side-label">FOOD SUPPLEMENT</p>
    <div class="brand"><span class="brand-dot"></span>Brisk Supplements</div>
    <h2 class="product-name"><span class="product-name__main">PROTEIN</span><span class="product-name__sub">POWDER</span></h2>
    <p class="flavour-tag">Banana Ice Cream<br>Flavours</p>
    <div class="flavour-image" role="img" aria-label="Photo of a banana ice cream scoop with banana slices"></div>
    <div class="nutrition">
      <div class="nutrition-badge"><b>XXX</b><span>CALORIES PER SERVING</span></div>
      <div class="nutrition-badge"><b>XXX</b><span>CARBS PER SERVING</span></div>
      <div class="nutrition-badge"><b>XXX</b><span>PROTEIN PER SERVING</span></div>
    </div>
    <p class="net-weight">NT WT: 500g</p>
  </article>

</main>
</body>
</html>
```